Plastic Surgeon Needs a business card desing

I need a plastic surgeon business card, Im young , innovative , not afraid of thinking out of the box, What I dont like is human figures or scalpes as designing the card, because I think they are old fashion, I think my name is my strongest card, so I try to find the desing to be something elegant , simple , slick , stylish , radiant with carimsa!

Target Market(s)

PLastics Surgery Patients and doctors to have my data

Industry/Entity Type

Plastic

Contact Information for Business Card

phone numbers need to be legible , right now i have grey scales so they a not to legible

Font styles to use
Serif
Sans Serif

Requirements
Must have
• Personality, and it has to look like a doctor card, not a buisness man card, that is why i think it should be clean , clear , and legible
Nice to have
• Stylilsh, not to heavy card, in means of colors and logos, i think it should give a sensation of health
• Im not sure to have the logo of the hospital i work
Should not have
• human figures
• Hands
• Surgeons

```html
<!DOCTYPE html>
<html lang="es">
<head>
<meta charset="utf-8">
<title>Dr. Martín Olvera – Tarjeta de presentación</title>
<link rel="stylesheet" href="https://fonts.googleapis.com/css2?family=Open+Sans:wght@400;600;700&display=swap">
<style>
  :root {
    --navy: #1c3461;
    --silver: #b9bbbf;
    --silver-dark: #9a9da2;
    --paper: #ffffff;
    --ink: #1a1a1a;
    --backdrop: #e6e6e4;
  }
  * { box-sizing: border-box; margin: 0; padding: 0; }
  html, body {
    width: 1200px; height: 853px; overflow: hidden;
    background: var(--backdrop);
    font-family: "Open Sans", Arial, sans-serif;
  }
  .canvas { position: relative; width: 1200px; height: 853px; }

  .card-front {
    position: absolute; left: 90px; top: 370px;
    width: 605px; height: 340px;
    background: var(--navy);
    box-shadow: 0 4px 12px rgba(0,0,0,.18);
    display: flex; align-items: center; justify-content: center;
  }
  .card-front .brand-name {
    color: var(--silver);
    font-weight: 400; font-size: 52px; letter-spacing: 2px;
  }

  .card-back {
    position: absolute; left: 720px; top: 90px;
    width: 357px; height: 624px;
    background: var(--paper);
    box-shadow: 0 4px 12px rgba(0,0,0,.18);
  }
  .card-back .brand-name {
    position: absolute; left: 0; right: 0; top: 150px;
    text-align: center;
    color: var(--silver-dark);
    font-weight: 400; font-size: 48px; letter-spacing: 2px;
  }
  .doctor-name {
    position: absolute; left: 0; right: 0; top: 238px;
    text-align: center;
    color: var(--navy); font-weight: 700; font-size: 25px; letter-spacing: .3px;
  }
  .specialty {
    position: absolute; left: 0; right: 0; top: 268px;
    text-align: center; color: var(--ink); font-size: 14.5px;
  }

  .contact-row {
    position: absolute; left: 20px;
    display: flex; align-items: flex-start; gap: 22px;
    color: var(--ink); font-size: 16.5px; line-height: 20px;
  }
  .contact-row .icon {
    width: 25px; height: 25px; flex: none;
    background: var(--navy);
    display: flex; align-items: center; justify-content: center;
  }
  .contact-row .icon svg { width: 15px; height: 15px; fill: #fff; }
  .row-address { top: 343px; }
  .row-address .icon { margin-top: 18px; }
  .row-phone { top: 432px; }
  .row-mobile { top: 465px; }
  .row-mail { top: 499px; }
  .row-web { top: 532px; }
  .contact-row .label { padding-top: 2px; }

  .hospital-mark {
    position: absolute; left: 252px; top: 548px;
    display: flex; align-items: center; gap: 5px;
    color: var(--navy); font-size: 9.5px; font-weight: 400;
  }
  .hospital-mark .square { width: 10px; height: 10px; background: var(--navy); }

  .rule-silver {
    position: absolute; left: 0; right: 0; top: 584px; height: 4px;
    background: var(--silver);
  }
  .band-navy {
    position: absolute; left: 0; right: 0; bottom: 0; height: 30px;
    background: var(--navy);
  }
</style>
</head>
<body>
<div class="canvas">

  <section class="card-front">
    <span class="brand-name">Olvera</span>
  </section>

  <section class="card-back">
    <span class="brand-name">Olvera</span>
    <h1 class="doctor-name">DR. MARTÍN OLVERA</h1>
    <p class="specialty">Cirugia Plastica</p>

    <div class="contact-row row-address">
      <span class="icon"><svg viewBox="0 0 16 16"><path d="M8 1a5 5 0 0 0-5 5c0 3.6 5 9 5 9s5-5.4 5-9a5 5 0 0 0-5-5zm0 7a2 2 0 1 1 0-4 2 2 0 0 1 0 4z"/></svg></span>
      <span class="label">Calle Nogales 2150 Int 84<br>Torre Médica Alameda<br>Guadalajara, Jal, México</span>
    </div>

    <div class="contact-row row-phone">
      <span class="icon"><svg viewBox="0 0 16 16"><path d="M3.6 1.5l2.2 2.4-1.2 1.8c.9 2 2.6 3.7 4.6 4.6l1.8-1.2 2.4 2.2-1 2.2C7 13.2 2.8 9 1.4 2.5z"/></svg></span>
      <span class="label">01 (33) 35550142</span>
    </div>

    <div class="contact-row row-mobile">
      <span class="icon"><svg viewBox="0 0 16 16"><path d="M5 1h6v14H5zM6 3v8h4V3zm1.3 9.3h1.4v1.4H7.3z" fill-rule="evenodd"/></svg></span>
      <span class="label">33 5550 2718</span>
    </div>

    <div class="contact-row row-mail">
      <span class="icon"><svg viewBox="0 0 16 16"><path d="M1.5 4h13v8h-13zM2.5 4.8L8 9l5.5-4.2v.9L8 10 2.5 5.7z" fill-rule="evenodd"/></svg></span>
      <span class="label">martin@drolvera.com</span>
    </div>

    <div class="contact-row row-web">
      <span class="icon"><svg viewBox="0 0 16 16"><path d="M8 1.5a6.5 6.5 0 1 0 0 13 6.5 6.5 0 0 0 0-13zm-.6 1.3v2.5H5.2c.5-1.3 1.3-2.2 2.2-2.5zm1.2 0c.9.3 1.7 1.2 2.2 2.5H8.6zM4.9 6.5h2.5v2.9H4.9zm3.7 0h2.5v2.9H8.6zM3 6.5h.7v2.9H3a5 5 0 0 1 0-2.9zm9.3 0h.7a5 5 0 0 1 0 2.9h-.7zM5.2 10.6h2.2v2.5c-.9-.3-1.7-1.2-2.2-2.5zm3.4 0h2.2c-.5 1.3-1.3 2.2-2.2 2.5z"/></svg></span>
      <span class="label">www.drolvera.com</span>
    </div>

    <div class="hospital-mark">
      <span class="square"></span>
      <span>Hospitales Alameda</span>
    </div>

    <div class="rule-silver"></div>
    <div class="band-navy"></div>
  </section>

</div>
</body>
</html>
```